Marta Belle Designs & Events business card

I need an elegant informative but not busy business card using my logo. We are a florist with high end customers. I am adding a PDF file and a PNG file for those who requested it
Updates

Target Market(s)

Brides, grooms, men purchasing flowers
Ages 20-65

Industry/Entity Type

Florist

Requirements
Must have
• Business info:
Marta Belle Design & Events
www.martabelleevents-sample.com.
555-418-2763

555-418-2763
Nice to have
• Est 1968
may want Pinterest logo, twitter and linkedin and facbook
Should not have
• Clip art or photos

```html
<!DOCTYPE html>
<html lang="en">
<head>
<meta charset="utf-8">
<title>Marta Belle Designs &amp; Events — Business Cards</title>
<link rel="stylesheet" href="https://fonts.googleapis.com/css2?family=Cinzel:wght@400;500&family=Jost:wght@400&display=swap">
<style>
  :root {
    --backdrop: #9c9c9c;
    --paper: #fbf9f9;
    --ink: #1b1b1b;
    --black-card: #0c0c0c;
    --blush: #ec9fb0;
    --blush-pale: #f6dbe1;
    --blush-deep: #e07f96;
    --white: #ffffff;
  }
  * { margin: 0; padding: 0; box-sizing: border-box; }
  html, body { width: 1200px; height: 1125px; overflow: hidden; }
  body { background: var(--backdrop); position: relative; font-family: "Jost", sans-serif; }

  .card {
    position: absolute;
    width: 470px;
    height: 290px;
    overflow: hidden;
    box-shadow: 0 2px 5px rgba(0,0,0,.35);
  }
  .card--back-light  { left: 117px; top: 267px; background: var(--paper); }
  .card--front-light { left: 645px; top: 267px; background: var(--paper); }
  .card--back-dark   { left: 117px; top: 598px; background: var(--black-card); }
  .card--front-dark  { left: 645px; top: 598px; background: var(--black-card); }

  /* back side */
  .pattern-field { position: absolute; inset: 0; }
  .card--back-light .pattern-field { background: linear-gradient(180deg, var(--blush-pale), #fbeef1); opacity: .7; }
  .card--back-dark .pattern-field { background: linear-gradient(180deg, #161616, #0a0a0a); }

  .mark {
    position: absolute; left: 0; right: 0; top: 116px;
    display: flex; align-items: center; justify-content: center; gap: 10px;
    font-family: "Cinzel", serif; font-weight: 500; font-size: 30px; line-height: 38px; letter-spacing: 2px;
  }
  .mark__dot { width: 12px; height: 12px; border-radius: 50%; }
  .card--back-light .mark { color: var(--ink); }
  .card--back-light .mark__dot { background: var(--ink); }
  .card--back-dark .mark { color: var(--blush-pale); }
  .card--back-dark .mark__dot { background: var(--blush-pale); }

  .social {
    position: absolute; left: 0; right: 0; top: 211px;
    text-align: center; font-size: 11.8px; line-height: 19px;
  }
  .card--back-light .social { color: var(--ink); }
  .card--back-dark .social { color: var(--blush); }

  /* front side */
  .ornament-field { position: absolute; left: 0; top: 0; width: 270px; height: 290px; }
  .card--front-light .ornament-field { background: radial-gradient(circle at 120px 145px, var(--blush-pale) 0%, rgba(246,219,225,.4) 55%, rgba(251,249,249,0) 80%); }
  .card--front-dark .ornament-field { background: radial-gradient(circle at 120px 145px, #2c2c2c 0%, #1a1a1a 55%, rgba(12,12,12,0) 80%); }

  .brand { position: absolute; left: 20px; width: 206px; top: 142px; text-align: center; }
  .brand__name {
    display: block; font-family: "Cinzel", serif; font-weight: 400;
    font-size: 21px; letter-spacing: 3px; line-height: 26px; white-space: nowrap;
  }
  .brand__line { display: block; font-size: 8.5px; line-height: 12px; letter-spacing: 2.6px; margin-top: 2px; }
  .brand__trade { display: block; font-family: "Cinzel", serif; font-size: 12px; line-height: 14px; letter-spacing: 1px; }
  .brand__year { display: block; font-size: 11px; line-height: 13px; letter-spacing: .5px; }
  .card--front-light .brand__name,
  .card--front-light .brand__trade { color: var(--ink); }
  .card--front-light .brand__line,
  .card--front-light .brand__year { color: var(--blush-deep); }
  .card--front-dark .brand__name,
  .card--front-dark .brand__trade,
  .card--front-dark .brand__year { color: var(--white); }
  .card--front-dark .brand__line { color: var(--blush); }

  .contact { position: absolute; right: 24px; top: 192px; text-align: right; }
  .contact__name {
    font-family: "Cinzel", serif; font-size: 20px; letter-spacing: .5px; line-height: 24px;
    color: var(--blush);
  }
  .contact__line { font-size: 14px; line-height: 16.5px; letter-spacing: .2px; }
  .card--front-light .contact__line { color: var(--ink); }
  .card--front-dark .contact__line { color: var(--white); }
</style>
</head>
<body>

  <section class="card card--back-light">
    <div class="pattern-field" role="img" aria-label="Repeating pale pink monogram and scroll pattern"></div>
    <div class="mark"><span class="mark__dot"></span>Marta Belle</div>
    <p class="social">
      photoshare-sample.com/martabelleevents &nbsp;friendpage-sample.com/martabelleevents<br>
      chirpline-sample.com/martabelleevents &nbsp;pinboard-sample.com/martabelleevents<br>
      proflink-sample.com/in/marta-belle-designs/x7k/2q9/
    </p>
  </section>

  <section class="card card--front-light">
    <div class="ornament-field" role="img" aria-label="Large pink floral scroll ornament"></div>
    <div class="brand">
      <span class="brand__name">Marta Belle</span>
      <span class="brand__line">DESIGNS &amp; EVENTS</span>
      <span class="brand__trade">FLOWERS</span>
      <span class="brand__year">Est 1968</span>
    </div>
    <div class="contact">
      <p class="contact__name">Nora Whitfield</p>
      <p class="contact__line">555-418-2763</p>
      <p class="contact__line">www.martabelleevents-sample.com</p>
      <p class="contact__line">martabelleevents@sample-mail.com</p>
    </div>
  </section>

  <section class="card card--back-dark">
    <div class="pattern-field" role="img" aria-label="Repeating dark monogram and scroll pattern"></div>
    <div class="mark"><span class="mark__dot"></span>Marta Belle</div>
    <p class="social">
      photoshare-sample.com/martabelleevents &nbsp;friendpage-sample.com/martabelleevents<br>
      chirpline-sample.com/martabelleevents &nbsp;pinboard-sample.com/martabelleevents<br>
      proflink-sample.com/in/marta-belle-designs/x7k/2q9/
    </p>
  </section>

  <section class="card card--front-dark">
    <div class="ornament-field" role="img" aria-label="Large dark grey floral scroll ornament"></div>
    <div class="brand">
      <span class="brand__name">Marta Belle</span>
      <span class="brand__line">DESIGNS &amp; EVENTS</span>
      <span class="brand__trade">FLOWERS</span>
      <span class="brand__year">Est 1968</span>
    </div>
    <div class="contact">
      <p class="contact__name">Nora Whitfield</p>
      <p class="contact__line">555-418-2763</p>
      <p class="contact__line">www.martabelleevents-sample.com</p>
      <p class="contact__line">martabelleevents@sample-mail.com</p>
    </div>
  </section>

</body>
</html>
```